Journeys With Marlowe Business Cards

I need a business card design for my upscale Travel Agency.
Attached you can find my logo.
I would like to include the following:
- Name
- Title
- Phone Number
- Email
- Website
- and then something like: Follow us: JourneysWithMarlowe (and then social media icons in color).
The logo should be in the front and then also the back.
I am also attaching a design that I liked (mostly for the layout) but open to any suggestions
Industry/Entity Type
Travel Agent
Contact Information for Business Card
Name: Celine Drummond
Title: Travel Designer / Owner
Phone: 415-296-0487
Email: celine@journeyswithmarlowe.example
Website: www.JourneysWithMarlowe.example
Social Media Handles for FB,IG, Pulse: JourneysWithMarlowe
Font styles to use
Colors
Designer to choose colors to be used in the design.
Look and feel

```html
<!DOCTYPE html>
<html lang="en">
<head>
<meta charset="utf-8">
<title>Journeys With Marlowe — Business Cards</title>
<link rel="stylesheet" href="https://fonts.googleapis.com/css2?family=Oswald:wght@400;600&family=Montserrat:wght@300;400&display=swap">
<style>
  :root {
    --backdrop: #2b2b2b;
    --card-black: #0b0b0b;
    --card-white: #ececec;
    --gold: #f2bd6b;
    --ink: #111111;
    --ink-soft: #333333;
    --rule: #8a8a8a;
  }
  * { box-sizing: border-box; margin: 0; padding: 0; }
  html, body { width: 1200px; height: 900px; overflow: hidden; }
  body {
    background: var(--backdrop);
    display: flex;
    flex-direction: column;
    align-items: center;
    justify-content: center;
    gap: 24px;
  }
  .card {
    position: relative;
    width: 720px;
    height: 411px;
    overflow: hidden;
  }

  /* Back */
  .card--back { background: var(--card-black); }
  .card__pattern {
    position: absolute; inset: 0;
    background: radial-gradient(ellipse at 70% 30%, #1c1c1c 0%, #0d0d0d 60%, #070707 100%);
  }
  .follow {
    position: absolute; left: 52px; top: 258px;
  }
  .follow__handle {
    font-family: "Oswald", sans-serif;
    font-weight: 600;
    font-size: 20px;
    letter-spacing: 2px;
    color: var(--gold);
    text-transform: uppercase;
  }
  .follow__networks {
    display: flex; gap: 14px; margin-top: 8px; margin-left: 24px;
  }
  .network {
    display: flex; align-items: center; gap: 5px;
    font-family: "Oswald", sans-serif; font-weight: 400; font-size: 11px;
    color: #d8d8d8; letter-spacing: 0.5px;
  }
  .network__dot { width: 12px; height: 12px; border-radius: 50%; background: #d8d8d8; }

  .brand {
    display: flex; align-items: center; gap: 14px;
    font-family: "Oswald", sans-serif; font-weight: 600;
    color: var(--gold);
  }
  .brand__mark { background: var(--gold); flex: none; }
  .card--back .brand { position: absolute; right: 48px; bottom: 62px; font-size: 30px; }
  .card--back .brand__mark { width: 26px; height: 26px; }

  /* Front */
  .card--front { background: var(--card-white); }
  .card--front .brand {
    position: absolute; top: 66px; left: 0; right: 0; justify-content: center;
    font-size: 40px;
  }
  .card--front .brand__mark { width: 34px; height: 34px; }
  .person {
    position: absolute; top: 168px; left: 0; right: 0; text-align: center;
    font-family: "Oswald", sans-serif;
  }
  .person__name {
    display: inline-block;
    font-weight: 600; font-size: 36px; letter-spacing: 3px; color: var(--ink);
    text-transform: uppercase; line-height: 1.1;
    padding: 0 6px 4px;
    border-bottom: 1px solid var(--rule);
  }
  .person__title {
    margin-top: 4px;
    font-weight: 600; font-size: 14px; letter-spacing: 2px; color: var(--ink);
    text-transform: uppercase;
  }
  .contacts {
    position: absolute; left: 0; right: 0; bottom: 46px;
    display: grid; grid-template-columns: 1fr 1.5fr 1.5fr;
    align-items: end;
  }
  .contact {
    text-align: center;
    font-family: "Montserrat", sans-serif; font-weight: 300; font-size: 14px;
    color: var(--ink-soft);
    padding: 10px 4px 0;
  }
  .contact + .contact { border-left: 1px solid var(--rule); }
  .contact__icon { display: block; margin: 0 auto 6px; width: 22px; height: 22px; fill: var(--ink); }
</style>
</head>
<body>

  <section class="card card--back" aria-label="Card back">
    <div class="card__pattern" role="img" aria-label="Repeating faint monogram pattern across the dark card"></div>
    <div class="follow">
      <p class="follow__handle">JourneysWithMarlowe</p>
      <div class="follow__networks">
        <span class="network"><span class="network__dot"></span>Linkup</span>
        <span class="network"><span class="network__dot"></span>Pulse</span>
        <span class="network"><span class="network__dot"></span>Frame</span>
      </div>
    </div>
    <div class="brand"><span class="brand__mark"></span><span class="brand__name">Journeys With Marlowe</span></div>
  </section>

  <section class="card card--front" aria-label="Card front">
    <div class="brand"><span class="brand__mark"></span><span class="brand__name">Journeys With Marlowe</span></div>
    <div class="person">
      <h1 class="person__name">Celine Drummond</h1>
      <p class="person__title">Travel Designer / Owner</p>
    </div>
    <div class="contacts">
      <p class="contact contact--phone">
        <svg class="contact__icon" viewBox="0 0 24 24" aria-hidden="true"><path d="M6.6 10.8c1.4 2.8 3.8 5.1 6.6 6.6l2.2-2.2c.3-.3.7-.4 1-.2 1.1.4 2.3.6 3.6.6.6 0 1 .4 1 1V20c0 .6-.4 1-1 1C10.6 21 3 13.4 3 4c0-.6.4-1 1-1h3.5c.6 0 1 .4 1 1 0 1.3.2 2.5.6 3.6.1.3 0 .7-.2 1z"/></svg>
        415-296-0487
      </p>
      <p class="contact contact--email">
        <svg class="contact__icon" viewBox="0 0 24 24" aria-hidden="true"><path d="M2 5h20v14H2zm2 2v.5l8 5.5 8-5.5V7zm0 2.9V17h16V9.9l-8 5.5z"/></svg>
        celine@journeyswithmarlowe.example
      </p>
      <p class="contact contact--web">
        <svg class="contact__icon" viewBox="0 0 24 24" aria-hidden="true"><path d="M12 3 2 12h3v8h5v-5h4v5h5v-8h3z"/></svg>
        www.JourneysWithMarlowe.example
      </p>
    </div>
  </section>

</body>
</html>
```